Copperline Real Estate Company needs Website

I need an updated, easy to use website for my Real Estate company based out of Amarillo, TX.
Our current focus is on residential rental properties. However we are looking to expand into multi-family rentals, commercial rentals, and vacation rentals.
We also offer Real Estate Listing services.
The final design should be user friendly.

Target Market(s)

Homeowners and renters

Industry/Entity Type

Real Estate

Coding

Coded - Design and coding required

Number of Pages Required

1 page

Font styles to use
Sans Serif

Requirements
Must have
• Easy to navigate

```html
<!DOCTYPE html>
<html lang="en">
<head>
<meta charset="utf-8">
<title>Copperline Real Estate Company</title>
<link href="https://fonts.googleapis.com/css2?family=Montserrat:wght@300;400;600;700;800&family=Open+Sans:wght@400;600&display=swap" rel="stylesheet">
<style>
:root{
  --blue:#1a9ad6;
  --ink:#222831;
  --muted:#8a8f96;
  --line:#d5d8dc;
  --navy:#2a3a78;
  --dark:#2b2b2e;
  --white:#ffffff;
}
*{margin:0;padding:0;box-sizing:border-box}
html,body{width:1200px;height:1120px;overflow:hidden;background:var(--white)}
body{font-family:"Open Sans",Arial,sans-serif;color:var(--ink)}
.page{position:absolute;left:409px;top:0;width:383px;height:1120px;background:var(--white)}
.abs{position:absolute}
.heading{font-family:"Montserrat",Arial,sans-serif;font-weight:300;letter-spacing:.5px;text-align:center;width:100%;left:0}
.heading b{font-weight:700;color:var(--blue)}
.dots{left:0;width:100%;display:flex;justify-content:center;gap:2px}
.dots span{width:3px;height:3px;border-radius:50%;background:#c6c9cd}
.dots.light span{background:var(--white)}

/* header */
.phone{left:48px;top:19px;font:700 4.6px "Montserrat",sans-serif;display:flex;align-items:center;gap:2px}
.phone-mail{left:48px;top:26px;font-size:3px;color:var(--muted)}
.brand{left:0;width:100%;top:10px;text-align:center;font:700 15px "Montserrat",sans-serif;color:var(--blue);letter-spacing:.2px}
.search{left:276px;top:21px}
.find-agent{left:287px;top:19px;width:42px;height:10px;border-radius:6px;background:var(--blue);color:var(--white);font:700 3.4px "Montserrat",sans-serif;display:flex;align-items:center;justify-content:center;gap:2px}
.nav{top:43px;left:0;width:100%;font:600 3.6px "Montserrat",sans-serif;color:#c9ccd0}
.nav span{position:absolute;transform:translateX(-50%);white-space:nowrap}
.nav .active{color:var(--ink)}
.nav-underline{left:52px;top:49px;width:19px;height:1.2px;background:var(--blue)}

/* hero */
.hero{left:0;top:56px;width:383px;height:172px;background:linear-gradient(180deg,#3d5fa8 0%,#6a86c2 45%,#273d7a 80%,#1a2350 100%)}
.hero-title{left:49px;top:107px;width:140px;height:44px;background:rgba(90,96,105,.82);padding:4px 5px 0}
.hero-title .name{font:800 18.5px/1 "Montserrat",sans-serif;color:var(--white);letter-spacing:.3px}
.hero-title .sub{font:300 8px "Montserrat",sans-serif;color:#b7bcc3;text-align:right;margin-top:3px;letter-spacing:.5px}
.hero-caption{left:49px;top:154px;width:126px;height:16px;background:rgba(90,96,105,.82);color:#e4e6ea;font-size:3.2px;line-height:4px;padding:3px 5px}
.hero-next{left:177px;top:154px;width:12px;height:16px;background:rgba(90,96,105,.82);display:flex;align-items:center;justify-content:center}
.hero-dots{left:329px;top:213px;display:flex;gap:2px}
.hero-dots span{width:3.5px;height:3.5px;border-radius:50%;background:var(--blue)}
.hero-dots span:first-child{background:var(--white);box-shadow:0 0 0 .8px var(--blue)}

/* welcome */
.welcome-title{top:244px;font-size:10.5px}
.welcome-dots{top:264px}
.welcome-copy{left:64px;width:255px;text-align:center;font-size:3.6px;line-height:7.2px;color:#6b7078}
.btn-outline{left:159px;width:64px;height:13px;border:1.3px solid var(--blue);border-radius:8px;font-size:3.6px;color:var(--muted);display:flex;align-items:center;justify-content:center}

/* services */
.services{left:0;top:385px;width:383px;height:241px;background:linear-gradient(180deg,#3a3e45 0%,#2a3140 40%,#36404f 60%,#1d2533 100%)}
.services-title{top:407px;font-size:10px;color:var(--white)}
.services-dots{top:430px}
.service{width:96px;text-align:center;color:var(--white);transform:translateX(-50%)}
.service svg{display:block;margin:0 auto 4px}
.service h3{font:700 6.6px "Montserrat",sans-serif;letter-spacing:.2px;margin-bottom:2px}
.service p{font-size:3.4px;line-height:4.6px;color:#e5e7ea}

/* latest property */
.latest-title{top:643px;font-size:10px}
.latest-dots{top:662px}
.card-img{width:102px;height:79px;top:678px;border:1.5px solid var(--navy)}
.card-name{top:762px;font:400 6px "Open Sans",sans-serif;color:#4a4f56}
.card-desc{top:773px;width:82px;font-size:3.3px;line-height:4.4px;color:#6b7078}
.card-meta{top:788px;width:82px;display:flex;gap:0;font-size:4px;color:var(--muted);align-items:center}
.card-meta span{display:flex;align-items:center;gap:1.5px;width:33%}

/* contact */
.contact{left:0;top:846px;width:383px;height:175px;background:linear-gradient(180deg,#3c414a 0%,#2f3642 45%,#1e242d 100%)}
.contact-title{top:868px;font-size:10px;color:var(--white)}
.contact-dots{top:888px}
.field{height:13px;border:1.3px solid var(--blue);border-radius:8px;font-size:3.4px;color:#c9ccd0;padding:0 8px;display:flex;align-items:center}
.field.message{height:28px;border-radius:12px}
.submit{left:159px;top:985px;width:64px;height:13px;border-radius:8px;background:var(--white);font-size:3.4px;color:var(--muted);display:flex;align-items:center;justify-content:center}

/* footer */
.foot-brand{left:35px;top:1034px;font:700 11px "Montserrat",sans-serif;color:var(--blue)}
.foot-copy{left:35px;top:1052px;width:100px;font-size:3.9px;line-height:7.2px;color:#555a61;text-align:justify}
.foot-label{top:1040px;font-size:4.4px;color:var(--blue)}
.contact-item{left:182px;display:flex;align-items:flex-start;gap:5px;font:600 3.3px/4.2px "Montserrat",sans-serif;color:var(--ink)}
.partner-badge{left:306px;top:1056px;width:33px;height:30px;background:var(--navy)}
.bottom-bar{left:0;top:1102px;width:383px;height:18px;background:var(--dark);color:#c9ccd0;font-size:3.3px;display:flex;align-items:center;justify-content:center}
</style>
</head>
<body>
<div class="page">

  <!-- header -->
  <div class="abs phone">
    <svg width="3" height="5" viewBox="0 0 3 5"><rect x=".3" y=".3" width="2.4" height="4.4" rx=".5" fill="none" stroke="#1a9ad6" stroke-width=".5"/></svg>
    806-555-0142
  </div>
  <div class="abs phone-mail">hello@copperlineproperties.com</div>
  <div class="abs brand">Copperline</div>
  <svg class="abs search" width="6" height="6" viewBox="0 0 6 6"><circle cx="2.5" cy="2.5" r="1.8" fill="none" stroke="#c9ccd0" stroke-width=".6"/><line x1="3.8" y1="3.8" x2="5.5" y2="5.5" stroke="#c9ccd0" stroke-width=".6"/></svg>
  <div class="abs find-agent">
    <svg width="6" height="3" viewBox="0 0 6 3"><path d="M0 1.5H5M3.8.4 5 1.5 3.8 2.6" fill="none" stroke="#fff" stroke-width=".5"/></svg>
    FIND AGENT
  </div>
  <nav class="abs nav">
    <span class="active" style="left:60px">HOME</span>
    <span style="left:109px">ABOUT US</span>
    <span style="left:162px">SERVICES</span>
    <span style="left:213px">LISTINGS</span>
    <span style="left:265px">TENANTS</span>
    <span style="left:318px">PARTNERS</span>
  </nav>
  <div class="abs nav-underline"></div>

  <!-- hero -->
  <div class="abs hero" role="img" aria-label="City skyline at dusk beside a modern glass-walled apartment balcony"></div>
  <div class="abs hero-title">
    <div class="name">COPPERLINE</div>
    <div class="sub">PROPERTIES</div>
  </div>
  <div class="abs hero-caption">Homes to rent and sell across Amarillo with a team you can trust.</div>
  <div class="abs hero-next"><svg width="3" height="5" viewBox="0 0 3 5"><path d="M.5.5 2.5 2.5.5 4.5" fill="none" stroke="#fff" stroke-width=".6"/></svg></div>
  <div class="abs hero-dots"><span></span><span></span><span></span><span></span></div>

  <!-- welcome -->
  <h2 class="abs heading welcome-title">WELCOME TO <b>COPPERLINE</b></h2>
  <div class="abs dots welcome-dots"><span></span><span></span><span></span></div>
  <p class="abs welcome-copy" style="top:275px">Copperline helps families across Amarillo find and keep the right home. We manage residential rentals with care, answer tenant calls quickly and keep every property in good repair. Our team is growing into multi-family, commercial and vacation rentals, and we also list homes for owners ready to sell. Whether you rent or own, we make each step simple and clear.</p>
  <p class="abs welcome-copy" style="top:318px">We know the local market street by street, and we price, show and lease homes with honest advice and steady follow-through from the first visit to the final signature.</p>
  <div class="abs btn-outline" style="top:352px">Read more</div>

  <!-- services -->
  <div class="abs services" role="img" aria-label="Night city skyscrapers reflected in a river"></div>
  <h2 class="abs heading services-title">OUR <b>SERVICES</b></h2>
  <div class="abs dots light services-dots"><span></span><span></span><span></span></div>

  <div class="abs service" style="left:66px;top:455px">
    <svg width="20" height="18" viewBox="0 0 20 18"><path d="M2 9 7 4h4l3 3-4 4-3-2M18 9l-5-5M5 12l3 3M8 11l3 3" fill="none" stroke="#fff" stroke-width="1.6" stroke-linecap="round"/></svg>
    <h3>YOUR HEADING</h3>
    <p>Clear guidance and steady support for owners and renters through every step of the process.</p>
  </div>
  <div class="abs service" style="left:191px;top:455px">
    <svg width="20" height="18" viewBox="0 0 20 18"><path d="M10 1 3 7v10h14V7z" fill="#fff"/><rect x="7" y="9" width="6" height="5" fill="#2a3140"/></svg>
    <h3>YOUR HEADING</h3>
    <p>Clear guidance and steady support for owners and renters through every step of the process.</p>
  </div>
  <div class="abs service" style="left:322px;top:455px">
    <svg width="20" height="18" viewBox="0 0 20 18"><circle cx="12" cy="5" r="3.5" fill="#fff"/><path d="M10 7 6 16M7.5 13l2 1M8.5 10.5l2 1" stroke="#fff" stroke-width="1.6" stroke-linecap="round"/></svg>
    <h3>YOUR HEADING</h3>
    <p>Clear guidance and steady support for owners and renters through every step of the process.</p>
  </div>
  <div class="abs service" style="left:66px;top:539px">
    <svg width="20" height="18" viewBox="0 0 20 18"><path d="M2 8 10 2l8 6" fill="none" stroke="#fff" stroke-width="1.6"/><path d="M5 15v-4l2-3h6l2 3v4z" fill="#fff"/><circle cx="7" cy="12.5" r="1" fill="#2a3140"/><circle cx="13" cy="12.5" r="1" fill="#2a3140"/></svg>
    <h3>YOUR HEADING</h3>
    <p>Clear guidance and steady support for owners and renters through every step of the process.</p>
  </div>
  <div class="abs service" style="left:191px;top:539px">
    <svg width="20" height="18" viewBox="0 0 20 18"><path d="M2 8 10 1l8 7" fill="none" stroke="#fff" stroke-width="1.6"/><path d="M12.5 7.5c0-1.2-1-1.8-2.5-1.8S7.5 6.4 7.5 7.6c0 2.6 5 1.6 5 4.3 0 1.2-1.1 1.9-2.5 1.9s-2.6-.7-2.6-1.9M10 4.5v12" fill="none" stroke="#fff" stroke-width="1.4"/></svg>
    <h3>YOUR HEADING</h3>
    <p>Clear guidance and steady support for owners and renters through every step of the process.</p>
  </div>
  <div class="abs service" style="left:322px;top:539px">
    <svg width="20" height="18" viewBox="0 0 20 18"><rect x="5" y="1" width="10" height="16" rx="1.5" fill="none" stroke="#fff" stroke-width="1.4"/><rect x="7" y="3" width="6" height="3" fill="#fff"/><g fill="#fff"><rect x="7" y="8" width="1.6" height="1.6"/><rect x="9.2" y="8" width="1.6" height="1.6"/><rect x="11.4" y="8" width="1.6" height="1.6"/><rect x="7" y="11" width="1.6" height="1.6"/><rect x="9.2" y="11" width="1.6" height="1.6"/><rect x="11.4" y="11" width="1.6" height="1.6"/><rect x="7" y="14" width="1.6" height="1.6"/><rect x="9.2" y="14" width="1.6" height="1.6"/><rect x="11.4" y="14" width="1.6" height="1.6"/></g></svg>
    <h3>YOUR HEADING</h3>
    <p>Clear guidance and steady support for owners and renters through every step of the process.</p>
  </div>

  <!-- latest property -->
  <h2 class="abs heading latest-title">LATEST <b>PROPERTY</b></h2>
  <div class="abs dots latest-dots"><span></span><span></span><span></span></div>

  <div class="abs card-img" style="left:23px;background:linear-gradient(180deg,#4a8fc4,#3f7d52 55%,#2e5a3a)" role="img" aria-label="Modern multi-storey apartment building with green balconies"></div>
  <div class="abs card-img" style="left:139px;background:linear-gradient(180deg,#1d2a5a,#6c5a7a 45%,#c89a5a 70%,#3a6fb0)" role="img" aria-label="Lit family house at dusk with a pool"></div>
  <div class="abs card-img" style="left:255px;background:linear-gradient(180deg,#3a4f8a,#9a8f86 45%,#c9b9a3 65%,#3aa0d8)" role="img" aria-label="Large stone mansion with pool in front"></div>

  <div class="abs card-name" style="left:23px">Property Name</div>
  <div class="abs card-name" style="left:139px">Property Name</div>
  <div class="abs card-name" style="left:255px">Property Name</div>
  <p class="abs card-desc" style="left:23px">A bright home close to schools and shopping.</p>
  <p class="abs card-desc" style="left:139px">A bright home close to schools and shopping.</p>
  <p class="abs card-desc" style="left:255px">A bright home close to schools and shopping.</p>

  <div class="abs card-meta" style="left:23px">
    <span><svg width="5" height="5" viewBox="0 0 5 5"><rect x=".4" y=".4" width="4.2" height="4.2" fill="none" stroke="#555" stroke-width=".7"/><path d="M.4.4l4.2 4.2M4.6.4.4 4.6" stroke="#555" stroke-width=".5"/></svg>150</span>
    <span style="justify-content:center"><svg width="4" height="5" viewBox="0 0 4 5"><path d="M2 0 4 2.5H0zM1 2.5h2V5H1z" fill="#555"/></svg>2</span>
    <span style="justify-content:flex-end"><svg width="10" height="4" viewBox="0 0 10 4"><path d="M0 0v4M10 1v3M0 2.5h10M1 1h8v1.5H1z" stroke="#333" stroke-width=".8" fill="#333"/></svg>3</span>
  </div>
  <div class="abs card-meta" style="left:139px">
    <span><svg width="5" height="5" viewBox="0 0 5 5"><rect x=".4" y=".4" width="4.2" height="4.2" fill="none" stroke="#555" stroke-width=".7"/><path d="M.4.4l4.2 4.2M4.6.4.4 4.6" stroke="#555" stroke-width=".5"/></svg>150</span>
    <span style="justify-content:center"><svg width="4" height="5" viewBox="0 0 4 5"><path d="M2 0 4 2.5H0zM1 2.5h2V5H1z" fill="#555"/></svg>2</span>
    <span style="justify-content:flex-end"><svg width="10" height="4" viewBox="0 0 10 4"><path d="M0 0v4M10 1v3M0 2.5h10M1 1h8v1.5H1z" stroke="#333" stroke-width=".8" fill="#333"/></svg>3</span>
  </div>
  <div class="abs card-meta" style="left:255px">
    <span><svg width="5" height="5" viewBox="0 0 5 5"><rect x=".4" y=".4" width="4.2" height="4.2" fill="none" stroke="#555" stroke-width=".7"/><path d="M.4.4l4.2 4.2M4.6.4.4 4.6" stroke="#555" stroke-width=".5"/></svg>150</span>
    <span style="justify-content:center"><svg width="4" height="5" viewBox="0 0 4 5"><path d="M2 0 4 2.5H0zM1 2.5h2V5H1z" fill="#555"/></svg>2</span>
    <span style="justify-content:flex-end"><svg width="10" height="4" viewBox="0 0 10 4"><path d="M0 0v4M10 1v3M0 2.5h10M1 1h8v1.5H1z" stroke="#333" stroke-width=".8" fill="#333"/></svg>3</span>
  </div>

  <div class="abs btn-outline" style="top:814px">View All</div>

  <!-- contact -->
  <div class="abs contact" role="img" aria-label="City skyline under a cloudy evening sky"></div>
  <h2 class="abs heading contact-title">CONTACT <b>US</b></h2>
  <div class="abs dots light contact-dots"><span></span><span></span><span></span></div>
  <div class="abs field" style="left:101px;top:909px;width:87px">Name</div>
  <div class="abs field" style="left:194px;top:909px;width:87px">Number</div>
  <div class="abs field" style="left:101px;top:929px;width:87px">Email</div>
  <div class="abs field" style="left:194px;top:929px;width:87px">Property</div>
  <div class="abs field message" style="left:101px;top:949px;width:180px">Message</div>
  <div class="abs submit">Submit</div>

  <!-- footer -->
  <div class="abs foot-brand">Copperline</div>
  <p class="abs foot-copy">Local rental management and listing services for homeowners and renters in Amarillo and the Texas Panhandle.</p>

  <div class="abs foot-label" style="left:182px">Contacts</div>
  <div class="abs contact-item" style="top:1055px">
    <svg width="5" height="5" viewBox="0 0 5 5"><path d="M1 .3 2 1.5 1.5 2.2c.4.9 1 1.5 1.8 1.8L4 3.5 4.7 4.5 4 5C2 4.8.2 3 0 1z" fill="#333"/></svg>
    806-555-0142
  </div>
  <div class="abs contact-item" style="top:1065px">
    <svg width="5" height="7" viewBox="0 0 5 7"><path d="M2.5 5C1 3.5.8 2.8.8 2.2a1.7 1.7 0 0 1 3.4 0C4.2 2.8 4 3.5 2.5 5z" fill="none" stroke="#333" stroke-width=".6"/><path d="M.5 6.5h4" stroke="#333" stroke-width=".6"/></svg>
    <span>1200 PLAINS AVE<br>AMARILLO TX</span>
  </div>
  <div class="abs contact-item" style="top:1081px">
    <svg width="6" height="5" viewBox="0 0 6 5"><rect x=".3" y=".5" width="5.4" height="4" fill="none" stroke="#333" stroke-width=".6"/><path d="M.3.5 3 2.8 5.7.5" fill="none" stroke="#333" stroke-width=".6"/></svg>
    HELLO@COPPERLINEPROPERTIES.COM
  </div>

  <div class="abs foot-label" style="left:304px">Partner</div>
  <div class="abs partner-badge" role="img" aria-label="Partner badge"></div>

  <div class="abs bottom-bar">© Copperline Properties. All rights reserved.</div>
</div>
</body>
</html>
```